Report Design

I am looking for a redesign of our monthly inspection reports we submit to our customers. I uploaded the current one we use (Tallowfern) and also that of a competitor (Cedar Knoll). I want to more copy the layout of the Cedarknoll report I attached but with more flow and design.

Requirements
Must have
• This has to be in a template format that we can modify the content every month.

```html
<!DOCTYPE html>
<html lang="en">
<head>
<meta charset="utf-8">
<title>Tallowfern – Landscape, Irr. &amp; Property Inspection</title>
<link rel="stylesheet" href="https://fonts.googleapis.com/css2?family=Arimo:wght@400;700&display=swap">
<style>
:root{
  --green:#2e8b4e;
  --green-dark:#23713e;
  --green-pale:#e4efe7;
  --page:#f7f7f6;
  --ink:#3a3a3a;
  --bg:#d9d9d9;
}
*{box-sizing:border-box;margin:0;padding:0}
html,body{width:1200px;height:820px;overflow:hidden;background:var(--bg);font-family:"Arimo",Arial,sans-serif;color:var(--ink)}
.spread{position:relative;width:1200px;height:820px}
.page{position:absolute;top:35px;width:580px;height:750px;background:var(--page);box-shadow:0 4px 14px rgba(0,0,0,.18);overflow:hidden}
.page--one{left:10px}
.page--two{left:610px}
.corner-tab{position:absolute;left:0;top:0;width:0;height:0;border-top:46px solid var(--green);border-right:34px solid transparent}
.brand{position:absolute;left:54px;top:30px}
.brand__name{display:flex;align-items:center;gap:7px;font-size:24px;font-weight:700;color:var(--green-dark);letter-spacing:-.3px}
.brand__mark{width:14px;height:14px;background:var(--green)}
.brand__tag{font-size:8.5px;font-weight:700;color:var(--ink);margin-top:3px;padding-left:21px}
.title-band{position:absolute;left:210px;top:0;width:230px;height:86px;background:var(--green-pale);display:flex;align-items:center;padding-left:18px}
.title-band h1{font-size:22px;line-height:1.1;font-weight:700;color:var(--green)}
.contact{position:absolute;left:440px;top:0;width:140px;height:86px;background:var(--green);color:#fff;font-size:7.5px;line-height:1.45;padding:12px 10px}
.contact strong{display:block;font-size:7.5px;margin-bottom:2px}
.contact__row{display:flex;align-items:flex-start;gap:4px}
.contact__row svg{flex:none;margin-top:1px}
.photo{position:absolute;border:1.5px solid var(--green);border-radius:10px;overflow:hidden}
.item{position:absolute;font-size:12.5px;line-height:1.3}
.item h2{font-size:13px;font-weight:700;color:var(--ink);margin-bottom:2px}
.item p{padding-left:18px}
.footer-line{position:absolute;left:40px;right:26px;top:690px;height:1.5px;background:var(--green)}
.page-number{position:absolute;right:30px;top:668px;font-size:12px;font-weight:700}
.footer-label{position:absolute;left:40px;top:700px;font-size:9px;font-weight:700;color:var(--green)}
</style>
</head>
<body>
<div class="spread">

  <section class="page page--one">
    <div class="corner-tab"></div>
    <div class="brand">
      <div class="brand__name"><span class="brand__mark"></span>Tallowfern</div>
      <div class="brand__tag">Landscape and Maintenance, Inc.</div>
    </div>
    <div class="title-band"><h1>Landscape, Irr. &amp;<br>Property Inspection</h1></div>
    <div class="contact">
      <strong>Landscape and Grounds<br>Maintenance Division</strong>
      <div class="contact__row"><svg width="7" height="9" viewBox="0 0 7 9"><path d="M3.5 0A3.2 3.2 0 0 0 .3 3.2C.3 5.6 3.5 9 3.5 9s3.2-3.4 3.2-5.8A3.2 3.2 0 0 0 3.5 0z" fill="#fff"/></svg><span>1184 Marlow Ridge Road<br>Pine Hollow, FL 30418</span></div>
      <div class="contact__row"><svg width="7" height="7" viewBox="0 0 7 7"><path d="M1 0l1.5 1.8-.8 1a4 4 0 0 0 1.8 1.8l1-.8L7 5.3 6 7A6 6 0 0 1 0 1z" fill="#fff"/></svg><span>555-014-0250</span></div>
      <div class="contact__row"><svg width="7" height="7" viewBox="0 0 7 7"><rect x="0" y="2" width="7" height="4" fill="#fff"/><rect x="1.5" y="0" width="4" height="2" fill="#fff"/></svg><span>Fax 555-019-4069</span></div>
    </div>

    <div class="item" style="left:40px;top:128px;width:180px">
      <h2>1.&nbsp; Grasses Throughout:</h2>
      <p>Right now the Muhly grass is blooming and looks great. The crew went around and trimmed them all up so they look fresh and clean. There were some of the types that were not blooming, that we trimmed back farther.</p>
    </div>
    <div class="photo" role="img" aria-label="Roadside bed of blooming pink Muhly grass with a young tree" style="left:232px;top:118px;width:330px;height:240px;background:linear-gradient(180deg,#dfe3e6 0%,#c8cfd2 35%,#8a9e6e 55%,#b4868f 68%,#6f8a45 85%,#7c7460 100%)"></div>
    <div class="photo" role="img" aria-label="Ornamental grasses beside a building wall" style="left:30px;top:372px;width:190px;height:112px;background:linear-gradient(135deg,#e4e0d8 0%,#cfc9bd 50%,#7f8b62 80%,#6b6455 100%)"></div>
    <div class="photo" role="img" aria-label="Main entrance median with crosswalk and apartment buildings" style="left:250px;top:388px;width:312px;height:240px;background:linear-gradient(180deg,#e2e5e8 0%,#cdd2d6 30%,#5f6a5e 50%,#4f5a46 62%,#8a8d8f 75%,#a9abab 100%)"></div>
    <div class="item" style="left:40px;top:560px;width:200px">
      <h2>2.&nbsp; Flowers:</h2>
      <p>Both main entrances are in need of fresh flowers.</p>
    </div>

    <div class="page-number">1</div>
    <div class="footer-line"></div>
    <div class="footer-label">Landscape, Irr. &amp; Property Inspection</div>
  </section>

  <section class="page page--two">
    <div class="corner-tab"></div>
    <div class="brand">
      <div class="brand__name"><span class="brand__mark"></span>Tallowfern</div>
      <div class="brand__tag">Landscape and Maintenance, Inc.</div>
    </div>
    <div class="title-band"><h1>Landscape, Irr. &amp;<br>Property Inspection</h1></div>
    <div class="contact">
      <strong>Landscape and Grounds<br>Maintenance Division</strong>
      <div class="contact__row"><svg width="7" height="9" viewBox="0 0 7 9"><path d="M3.5 0A3.2 3.2 0 0 0 .3 3.2C.3 5.6 3.5 9 3.5 9s3.2-3.4 3.2-5.8A3.2 3.2 0 0 0 3.5 0z" fill="#fff"/></svg><span>1184 Marlow Ridge Road<br>Pine Hollow, FL 30418</span></div>
      <div class="contact__row"><svg width="7" height="7" viewBox="0 0 7 7"><path d="M1 0l1.5 1.8-.8 1a4 4 0 0 0 1.8 1.8l1-.8L7 5.3 6 7A6 6 0 0 1 0 1z" fill="#fff"/></svg><span>555-014-0250</span></div>
      <div class="contact__row"><svg width="7" height="7" viewBox="0 0 7 7"><rect x="0" y="2" width="7" height="4" fill="#fff"/><rect x="1.5" y="0" width="4" height="2" fill="#fff"/></svg><span>Fax 555-019-4069</span></div>
    </div>

    <div class="item" style="left:40px;top:118px;width:180px">
      <h2>3.&nbsp; Palms Need<br>&nbsp;&nbsp;&nbsp;&nbsp;&nbsp;Trimming:</h2>
      <p>All the Palms could use a trimming, there are dead frons and some hanging seed pods and boots. Let us know if and when you would like to get this scheduled.</p>
    </div>
    <div class="photo" role="img" aria-label="Row of palm trees along a median beside a parking lot" style="left:232px;top:108px;width:330px;height:218px;background:linear-gradient(180deg,#e1e5e8 0%,#cfd5d8 30%,#5d7a52 52%,#7d8a6c 70%,#8d9092 85%,#6a7a4e 100%)"></div>
    <div class="photo" role="img" aria-label="Palm tree with dead fronds near a parking area" style="left:30px;top:298px;width:190px;height:112px;background:linear-gradient(180deg,#e3e6e8 0%,#cdd3d5 40%,#4f6a45 60%,#7f8a70 100%)"></div>
    <div class="item" style="left:40px;top:432px;width:180px">
      <h2>4.&nbsp; Fill In:</h2>
      <p>We should fill this corner in where truck run over the corner with additional plants.</p>
    </div>
    <div class="photo" role="img" aria-label="Corner planting bed with shrubs and a small tree beside a parking lot" style="left:250px;top:340px;width:312px;height:240px;background:linear-gradient(180deg,#e4e7e9 0%,#d2d6d8 35%,#9aa39a 50%,#4f6f3f 70%,#5d7b45 85%,#6b5a4c 100%)"></div>

    <div class="page-number">2</div>
    <div class="footer-line"></div>
    <div class="footer-label">Landscape, Irr. &amp; Property Inspection</div>
  </section>

</div>
</body>
</html>
```